Business Card Design

I'm a fishing guide needing a clean, concise design for my business. I'd like to use the cover photo and font design from my website for the background of the business card. My website is:
www.tidewrenoutfitters.com

Industry/Entity Type

Business

Contact Information for Business Card

Capt. Dale Penrow
Fly, Light Tackle, Conventional Gear
Gamefish of Massachusetts
website: www.tidewrenoutfitters.com
cell: 508-461-2297
email: dale@tidewrenoutfitters.com

```html
<!DOCTYPE html>
<html lang="en">
<head>
<meta charset="utf-8">
<title>Tidewren Outfitters – Business Card</title>
<link rel="stylesheet" href="https://fonts.googleapis.com/css2?family=Lato:wght@400;700;900&display=swap">
<style>
  :root {
    --page-bg: #e9e7e3;
    --steel-light: #c9cccd;
    --steel-mid: #aeb6b7;
    --steel-teal: #9fb2b1;
    --charcoal: #4a4d50;
    --charcoal-dark: #3a3c3f;
    --navy: #10101e;
    --navy-ink: #1b2233;
    --band-grey: #5c6262;
    --white: #ffffff;
    --photo-violet: #6c5f86;
    --photo-deep: #3f3a55;
    --photo-skin: #d9897a;
    --badge-green: #8fb36a;
    --badge-red: #d63b3b;
    --badge-yellow: #f1c232;
  }
  * { box-sizing: border-box; margin: 0; padding: 0; }
  html, body { width: 1200px; height: 918px; overflow: hidden; }
  body {
    background: var(--page-bg);
    font-family: "Lato", sans-serif;
    display: flex;
    flex-direction: column;
    align-items: center;
    justify-content: center;
    gap: 38px;
  }
  .card {
    position: relative;
    width: 700px;
    height: 400px;
    overflow: hidden;
    box-shadow: 0 6px 18px rgba(0,0,0,.18);
  }

  /* ---------- Front ---------- */
  .card-front {
    background: linear-gradient(100deg, var(--steel-light) 0%, var(--steel-mid) 55%, var(--steel-teal) 100%);
  }
  .front-name {
    position: absolute;
    top: 72px;
    left: 330px;
    font-size: 26px;
    color: var(--navy-ink);
    letter-spacing: .3px;
  }
  .front-name .title { font-weight: 900; }
  .front-name .person { font-weight: 400; }
  .front-specialty {
    position: absolute;
    top: 112px;
    left: 318px;
    right: 0;
    background: var(--navy);
    color: var(--white);
    font-size: 13px;
    padding: 7px 14px;
    line-height: 1.35;
  }
  .logo-panel {
    position: absolute;
    left: 0;
    bottom: 0;
    width: 218px;
    height: 178px;
    background: linear-gradient(180deg, var(--charcoal) 0%, var(--charcoal-dark) 100%);
    display: flex;
    align-items: center;
    justify-content: center;
    gap: 8px;
  }
  .logo-mark {
    width: 12px; height: 12px;
    border-radius: 50%;
    background: var(--steel-light);
  }
  .logo-name {
    color: var(--steel-light);
    font-size: 17px;
    font-weight: 400;
    letter-spacing: 1px;
    text-transform: uppercase;
    line-height: 1.2;
    text-align: center;
  }
  .company-band {
    position: absolute;
    left: 226px;
    right: 0;
    bottom: 132px;
    height: 46px;
    background: linear-gradient(90deg, var(--band-grey) 0%, var(--charcoal) 100%);
    color: var(--white);
    font-size: 28px;
    padding: 6px 14px;
    text-transform: uppercase;
  }
  .company-band .lead { font-weight: 400; }
  .company-band .tail { font-weight: 900; }
  .contact-block {
    position: absolute;
    left: 226px;
    right: 0;
    bottom: 0;
    height: 124px;
    background: var(--navy);
    color: var(--white);
    list-style: none;
    padding: 16px 14px;
    font-size: 14px;
    display: flex;
    flex-direction: column;
    gap: 12px;
  }

  /* ---------- Back ---------- */
  .card-back { background: var(--charcoal); }
  .hero-photo {
    position: absolute;
    top: 0; left: 0; right: 0;
    height: 268px;
    background:
      radial-gradient(ellipse at 92% 55%, var(--photo-skin) 0%, transparent 35%),
      radial-gradient(ellipse at 8% 8%, var(--photo-skin) 0%, transparent 28%),
      linear-gradient(110deg, var(--photo-deep) 0%, var(--photo-violet) 50%, var(--photo-deep) 100%);
  }
  .hero-logo {
    position: absolute;
    top: 40px;
    left: 40px;
    display: flex;
    align-items: center;
    gap: 10px;
    color: var(--white);
    font-size: 30px;
    font-weight: 400;
    letter-spacing: 2px;
    text-transform: uppercase;
  }
  .hero-logo .logo-mark { background: var(--white); width: 16px; height: 16px; }
  .url-band {
    position: absolute;
    left: 0; right: 0; bottom: 0;
    height: 132px;
    background: linear-gradient(180deg, var(--band-grey) 0%, var(--charcoal) 100%);
    display: flex;
    align-items: center;
    justify-content: space-between;
    padding: 0 28px;
    border-top: 4px solid var(--steel-light);
  }
  .url-band .url {
    color: var(--white);
    font-size: 30px;
    font-weight: 700;
    letter-spacing: .5px;
  }
  .partner-badges { display: flex; gap: 12px; align-items: center; }
</style>
</head>
<body>

  <!-- Front side -->
  <section class="card card-front" aria-label="Business card front">
    <h1 class="front-name"><span class="title">CAPT.</span> <span class="person">DALE PENROW</span></h1>
    <p class="front-specialty">Fly, Light Tackle, Conventional Gear Gamefish of Massachusetts</p>

    <div class="logo-panel">
      <span class="logo-mark"></span>
      <span class="logo-name">Tidewren<br>Outfitters</span>
    </div>

    <div class="company-band"><span class="lead">Tidewren</span> <span class="tail">Outfitters</span></div>

    <ul class="contact-block">
      <li>508-461-2297</li>
      <li>dale@tidewrenoutfitters.com</li>
      <li>www.tidewrenoutfitters.com</li>
    </ul>
  </section>

  <!-- Back side -->
  <section class="card card-back" aria-label="Business card back">
    <div class="hero-photo" role="img" aria-label="Photo of an angler holding a large tuna with a fly in its mouth"></div>
    <div class="hero-logo"><span class="logo-mark"></span>Tidewren Outfitters</div>

    <div class="url-band">
      <span class="url">www.tidewrenoutfitters.com</span>
      <div class="partner-badges" aria-label="Partner badges">
        <svg width="64" height="64" viewBox="0 0 64 64" aria-hidden="true">
          <circle cx="32" cy="32" r="30" fill="var(--badge-green)"/>
        </svg>
        <svg width="58" height="26" viewBox="0 0 58 26" aria-hidden="true">
          <rect width="58" height="26" rx="2" fill="var(--badge-red)"/>
        </svg>
        <svg width="40" height="40" viewBox="0 0 40 40" aria-hidden="true">
          <circle cx="20" cy="20" r="18" fill="var(--badge-yellow)"/>
        </svg>
      </div>
    </div>
  </section>

</body>
</html>
```